Brochure for a civil enineering company in A4 format

I need a brochure design for our company VELTA Engineering S.r.l.. We are an engineering consultant company. Our main clients are from the infrastructure industry (geotechnical and underground sectors mainly).
We are looking for a 2 pages (4 faces) fold out design with a glued pocket where we can put individual data sheets.
I need A4 format pages.

Target Market(s)

We are an engineering consultant company. Our main clients are from the infrastructure industry (geotechnical and underground sectors mainly).

Industry/Entity Type

Civil Engineer

Font styles to use
Sans Serif

Requirements
Must have
• Overall: 2 pages in A4 format
Essential style. Bright and modern appearance.
Glued pocket
Logo integrated in a picture on the pocket where I would like to insert a slogan (… velta engineering … reliable solutions …)
Attached are selected images which the designer can use and edit at their own discretion.
Some advice in the following (anyway designers are free to provide their solutions):
Outer sheets:
Front page with name, logo. It could be nice to have the “m” of the logo integrated in a pictures, also a modified picture (I mean modify one of the attached pictures) so to create a general image and do not tie the cover to a specific job.
Back page: offices address and contact email address. Nice to have one space for a slogan.
Inner sheet: text that I upload in the file “inside-sheets”, possibly with pictures on each sheet. In the right faces insert the glued pocket. On this pages insert the section OUR EXPERIENCE ….with a space for a picture of our team.
Nice to have
• Clean and essential design.
Pictures choosing from the atteched ones. Pictures could be modified in a very light manner to make them a general idea of the work ( I mean geotechnical world) without to be immediately linked to a specific site.
Should not have
• excessive frills

```html
<!DOCTYPE html>
<html lang="it">
<head>
<meta charset="utf-8">
<title>VELTA Engineering – Brochure, pagine interne</title>
<link href="https://fonts.googleapis.com/css2?family=Montserrat:wght@800&family=Didact+Gothic&display=swap" rel="stylesheet">
<style>
  :root{
    --canvas:#dedede;
    --ink:#111111;
    --paper:#ffffff;
    --panel-light:#e6e6e6;
    --panel-mid:#9a9a9a;
    --photo-dark-a:#2b2b2b;
    --photo-dark-b:#5d5d5d;
    --photo-light-a:#b9b9b9;
    --photo-light-b:#7c7c7c;
    --text-light:#f2f2f2;
    --text-dark:#1a1a1a;
  }
  *{box-sizing:border-box;margin:0;padding:0}
  html,body{width:1200px;height:840px;overflow:hidden;background:var(--canvas)}
  body{font-family:"Didact Gothic",sans-serif;display:flex;align-items:center;justify-content:center}
  .spread{width:1132px;height:800px;display:flex;box-shadow:0 6px 24px rgba(0,0,0,.25)}
  .page{position:relative;width:566px;height:800px;overflow:hidden;background:var(--paper)}
  .photo{position:absolute}
  .photo--dark{background:linear-gradient(160deg,var(--photo-dark-b),var(--photo-dark-a))}
  .photo--light{background:linear-gradient(170deg,var(--photo-light-a),var(--photo-light-b))}
  .title{font-family:"Montserrat",sans-serif;font-weight:800;text-transform:uppercase;line-height:.92;letter-spacing:.5px;color:var(--text-light)}
  .body-text{font-size:8.6px;line-height:1.38;color:var(--text-light)}
  .body-text p+p{margin-top:8px}
  .body-text--dark{color:var(--text-dark)}

  /* left page */
  .page--left .backdrop{inset:0}
  .company{position:absolute;left:34px;top:36px;width:280px}
  .company .title{font-size:36px;margin-bottom:16px}
  .company .body-text{padding-left:70px}
  .crane-photo{right:0;top:0;width:222px;height:230px}
  .services{position:absolute;left:330px;top:250px;width:216px}
  .services .title{font-size:30px;margin-bottom:12px}
  .services .body-text{width:112px;margin-left:104px}
  .site-photo{left:0;bottom:0;width:250px;height:270px}
  .help-box{position:absolute;right:0;bottom:0;width:316px;height:330px;background:var(--panel-mid);padding:26px 26px}

  /* right page */
  .expertise{position:absolute;left:0;top:0;width:362px;height:548px;background:var(--ink);padding:40px 26px 0 30px}
  .expertise .title{font-size:30px;margin-bottom:16px}
  .expertise .title span{font-size:22px}
  .partners{position:absolute;right:0;top:0;width:204px;height:400px;background:var(--panel-light);padding:40px 18px}
  .team-photo{right:0;top:400px;width:204px;height:148px}
  .pocket{left:0;bottom:0;width:566px;height:252px}
  .brand{position:absolute;right:34px;bottom:26px;text-align:right;color:var(--text-light)}
  .brand-name{font-family:"Didact Gothic",sans-serif;font-size:40px;line-height:1;letter-spacing:1px;display:flex;align-items:center;justify-content:flex-end;gap:8px}
  .brand-mark{width:10px;height:10px;border-radius:50%;background:var(--text-light)}
  .slogan{font-size:9px;margin-top:6px;letter-spacing:.5px}
</style>
</head>
<body>
<main class="spread">
  <section class="page page--left">
    <div class="photo photo--dark backdrop" role="img" aria-label="Cantiere di scavo in galleria, toni scuri"></div>
    <div class="photo photo--light crane-photo" role="img" aria-label="Gru e fresa meccanica in cantiere"></div>

    <div class="company">
      <h2 class="title">Our<br>Company</h2>
      <div class="body-text">
        <p>VELTA Engineering S.r.l. offre servizi di consulenza tecnica, contrattuale e strategica ai principali attori del settore delle scienze geologiche, dell'ingegneria geotecnica e idraulica. Lavoriamo con rigore per individuare la soluzione ottimale e aumentare la redditività del progetto.</p>
        <p>VELTA Engineering S.r.l. è una società indipendente nata nel luglio 2020 dall'associazione di un gruppo di professionisti con esperienza maturata in oltre trent'anni di attività come consulenti e direttori tecnici di Nordica Engineering.</p>
        <p>Each of our projects represents a long term commitment: we believe in providing safe, reliable, sustainable and innovative solutions. This is and will be our distinctive characteristic.</p>
      </div>
    </div>

    <div class="services">
      <h2 class="title">Our<br>Services</h2>
      <div class="body-text">
        <p>Progettazione e consulenza specialistica nel campo della geologia, della geotecnica, delle opere sotterranee e dell'ingegneria idraulica.</p>
      </div>
    </div>

    <div class="photo photo--light site-photo" role="img" aria-label="Cantiere con armature e scavo di fondazione"></div>

    <div class="help-box body-text body-text--dark">
      <p>Aiutiamo i nostri clienti a risolvere problemi di natura progettuale, contrattuale e costruttiva che possono nascere in ogni fase dell'opera, proponendo nuove idee e migliorando la qualità delle soluzioni adottate.</p>
      <p>VELTA Engineering è in grado di fornire la propria assistenza nell'intero iter, dalle indagini preliminari fino alla progettazione costruttiva e all'assistenza tecnica in fase di realizzazione.</p>
      <p>La specializzazione e l'esperienza accumulate nelle discipline della geologia e della geotecnica ci permettono di intervenire con efficacia quando sia necessario.</p>
      <p>Far fronte a situazioni di emergenza anche su progetti in fase avanzata, garantendo immediata focalizzazione e risultati in tempi brevi.</p>
      <p>Fornire "second opinion" di elevato valore tecnico ed economico, analizzare progetti svolti da terzi e individuarne le criticità principali.</p>
      <p>Ottimizzare i progetti esistenti, verificandone la cantierabilità e massimizzando l'efficacia economica degli investimenti.</p>
    </div>
  </section>

  <section class="page page--right">
    <div class="expertise">
      <h2 class="title"><span>Our</span> Expertise<br><span>and</span> Experience</h2>
      <div class="body-text">
        <p>La società nasce dall'associazione di un gruppo di professionisti con indiscusse competenze ed esperienza maturata in oltre trent'anni di attività come progettisti e consulenti nel settore delle grandi opere di ingegneria civile, geologia, geotecnica, idraulica ed opere sotterranee.</p>
        <p>I soci fondatori sono:</p>
        <p>Marco, già Direttore Tecnico e Socio di TORVA Srl, nel periodo di sua permanenza ha firmato i principali progetti nel campo delle opere sotterranee e della geotecnica. Può vantare la progettazione di oltre 150 gallerie naturali, numerose opere di sostegno e sistemazioni di versanti, con un valore complessivo delle opere che supera i 3.400 Mio EUR.</p>
        <p>Enrico, 30 anni di esperienza professionale. Coinvolto in più di 150 gallerie naturali con lunghezza complessiva superiore a 360 km. Numerosi progetti ed attività di assistenza tecnica nel campo delle strutture, delle sistemazioni idrogeologiche e della protezione ambientale. Ha svolto attività di verifica in Italia e all'estero per opere il cui valore supera i 1.400 Mio EUR.</p>
      </div>
    </div>

    <div class="partners body-text body-text--dark">
      <p>Serena, 30 anni di esperienza professionale. Coinvolta in più di 150 gallerie naturali con lunghezza complessiva superiore a 360 km. Numerosi progetti e attività di assistenza tecnica nel campo delle strutture e delle sistemazioni dei versanti, per opere il cui valore complessivo supera i 3.400 Mio EUR.</p>
      <p>Lucia, 30 anni di esperienza professionale. Coinvolta in più di 150 gallerie naturali con lunghezza complessiva superiore a 360 km. Responsabile di progetti di protezione ambientale e di assistenza alla costruzione in Italia e all'estero, per un valore complessivo superiore a 3.400 Mio EUR.</p>
    </div>

    <div class="photo photo--light team-photo" role="img" aria-label="Foto del team di VELTA Engineering"></div>

    <div class="photo photo--light pocket" role="img" aria-label="Tasca incollata con foto di cantiere, escavatore e palancole">
      <div class="brand">
        <div class="brand-name"><span class="brand-mark"></span>velta</div>
        <p class="slogan">… velta engineering … reliable solutions …</p>
      </div>
    </div>
  </section>
</main>
</body>
</html>
```